Equipment Finance Specialist I work with companies who need the funds to buy their equipment

I would like a business card that stands out on the shelves. I want to be able to hand it to someone and say WOW. This card should have my logo.
You can put color into it I am very open on design and color

What my company does is we deal with dealerships that sell equipment such as Dump Trucks garbage trucks tractors trailers. Customers get referred to us and depending on their time in business we will ask for the following items

Companies that have been in business for more than two years we have a credit application program up to 250K . With this program we need the following items Credit application filled out(which is what I would like to be able for the customer to click on my website to get.) as well as three current month bank statements.

Deals over 250k we will need the following items

2 years business tax returns
2 years personal tax returns
Profit & Loss statement
Personal Financial Statement

what we do
100% FINANCING
SEASONAL PAYMENTS
LOAN BALLOON PAYMENTS
TRAC LEASING
LOW-INTEREST REFINANCING RATES
DEBT CONSOLIDATION

We specialize in creative financing solutions and offer a variety of reliable, flexible and expandable lending choices.

Target Market(s)

Trucking Companies

Industry/Entity Type

Trucking Company

Contact Information for Business Card

* $250,000 Application only Program
* Loans from $30,000 to 5,000,000
* Competitive Interest Rates

Font styles to use
Serif
Sans Serif

Colors

Designer to choose colors to be used in the design.

Requirements
Must have
• On the back of the card.
• * $250,000 Application only Program
• * Loans from $30,000 to 5,000,000
• My name, email, website. address
• * Competitive Interest Rates
• * 100% Financing
Nice to have
• I want my logo to pop on the card
• My logo is the great one I would like to use
Should not have
• I am up for your creativity as well

```html
<!DOCTYPE html>
<html lang="en">
<head>
<meta charset="utf-8">
<title>Apex Lending – Business Card</title>
<link href="https://fonts.googleapis.com/css2?family=Montserrat:wght@500;800&family=Tinos:wght@700&display=swap" rel="stylesheet">
<style>
  :root {
    --backdrop: #2a2a2c;
    --card-dark: #1c1c1e;
    --card-dark-edge: #2f2f31;
    --silver: #d4d6d9;
    --paper: #ffffff;
    --navy: #1f2a6b;
    --red: #d9202c;
    --ink: #1a1a1a;
    --rule: #c9c9cc;
    --ghost: #ececee;
  }
  * { margin: 0; padding: 0; box-sizing: border-box; }
  html, body { width: 1200px; height: 900px; overflow: hidden; }
  body {
    background: var(--backdrop);
    font-family: "Montserrat", Arial, sans-serif;
    position: relative;
  }
  .card {
    position: absolute;
    left: 250px;
    width: 700px;
    height: 400px;
    overflow: hidden;
    box-shadow: 0 14px 30px rgba(0,0,0,.45);
  }
  /* Front */
  .card-front {
    top: 30px;
    background: radial-gradient(ellipse at 50% 45%, var(--card-dark-edge), var(--card-dark) 75%);
    display: flex;
    align-items: center;
    justify-content: center;
  }
  .brand {
    display: flex;
    align-items: center;
    gap: 18px;
  }
  .brand-dot {
    border-radius: 50%;
    flex: none;
  }
  .brand-name {
    font-weight: 800;
    text-transform: uppercase;
    letter-spacing: .02em;
    line-height: 1;
  }
  .card-front .brand-dot { width: 92px; height: 92px; border: 6px solid var(--silver); }
  .card-front .brand-name { color: var(--silver); font-size: 54px; }

  /* Back */
  .card-back { top: 470px; background: var(--paper); }
  .emblem-ghost {
    position: absolute;
    left: -40px;
    top: 90px;
    width: 330px;
    height: 330px;
    border-radius: 50%;
    background: radial-gradient(circle, var(--ghost) 0%, #f4f4f6 60%, rgba(255,255,255,0) 72%);
  }
  .card-back .brand {
    position: absolute;
    right: 60px;
    top: 46px;
    gap: 12px;
  }
  .card-back .brand-dot { width: 52px; height: 52px; border: 4px solid var(--navy); }
  .card-back .brand-name { color: var(--navy); font-size: 32px; }
  .divider {
    position: absolute;
    left: 110px;
    right: 40px;
    top: 140px;
    height: 1px;
    background: var(--rule);
  }
  .offer-list {
    position: absolute;
    right: 40px;
    top: 168px;
    list-style: none;
    text-align: right;
    color: var(--navy);
    font-weight: 500;
    font-size: 17px;
    line-height: 1.3;
  }
  .contact {
    position: absolute;
    left: 70px;
    top: 230px;
  }
  .person-name {
    font-family: "Tinos", "Times New Roman", serif;
    font-weight: 700;
    font-size: 24px;
    color: var(--ink);
    letter-spacing: -.01em;
  }
  .person-role {
    color: var(--navy);
    font-size: 17px;
    font-weight: 500;
    margin-bottom: 6px;
  }
  .contact-list { list-style: none; }
  .contact-list li {
    display: flex;
    align-items: center;
    gap: 10px;
    font-size: 17px;
    color: var(--ink);
    line-height: 1.35;
  }
  .contact-list svg { width: 14px; height: 14px; fill: var(--navy); flex: none; }
  .edge-bands { position: absolute; left: 0; bottom: 0; width: 700px; height: 40px; }
</style>
</head>
<body>

<section class="card card-front" aria-label="Card front">
  <div class="brand">
    <span class="brand-dot"></span>
    <span class="brand-name">Apex Lending</span>
  </div>
</section>

<section class="card card-back" aria-label="Card back">
  <div class="emblem-ghost" role="img" aria-label="Faint large company emblem in the background"></div>

  <div class="brand">
    <span class="brand-dot"></span>
    <span class="brand-name">Apex Lending</span>
  </div>

  <div class="divider"></div>

  <ul class="offer-list">
    <li>$250,000 Application only Program</li>
    <li>Loans from $30,000 to 5,000,000</li>
    <li>Competitive Interest Rates</li>
    <li>100% Financing</li>
  </ul>

  <div class="contact">
    <p class="person-name">YOUR NAME</p>
    <p class="person-role">Position</p>
    <ul class="contact-list">
      <li><svg viewBox="0 0 16 16"><path d="M3.5 1l2.5 3-1.5 1.8c.9 2 2.6 3.7 4.6 4.6L11 8.9l3 2.5-1.6 2.8C7 13.6 2.4 9 1.8 3.6z"/></svg>phone number</li>
      <li><svg viewBox="0 0 16 16"><path d="M1 3h14v10H1zm1.6 1.4v.3L8 8.6l5.4-3.9v-.3zM2.4 6.2v5.4h11.2V6.2L8 10.2z"/></svg>info@apexlending.com</li>
      <li><svg viewBox="0 0 16 16"><path d="M8 1a7 7 0 100 14A7 7 0 008 1zm-1 1.7v3.8H3a5.5 5.5 0 014-3.8zm2 0a5.5 5.5 0 014 3.8H9zM3 8.5h4v4.8a5.5 5.5 0 01-4-4.8zm6 0h4a5.5 5.5 0 01-4 4.8z"/></svg>apexlending.com</li>
      <li><svg viewBox="0 0 16 16"><path d="M8 1a5 5 0 00-5 5c0 3.8 5 9 5 9s5-5.2 5-9a5 5 0 00-5-5zm0 7a2 2 0 110-4 2 2 0 010 4z"/></svg>office address</li>
    </ul>
  </div>

  <svg class="edge-bands" viewBox="0 0 700 40" preserveAspectRatio="none" aria-hidden="true">
    <polygon points="0,34 420,34 405,40 0,40" fill="var(--navy)"/>
    <polygon points="420,34 440,22 700,22 700,40 405,40" fill="var(--red)"/>
  </svg>
</section>

</body>
</html>
```